Ad Design for a child care centre

Bright Pebbles Child Care Centre offers a safe, nurturing environment where your child will get the attention and care that he or she needs. Our ratio of children to adults is always within state guidelines - and often even higher - to make certain each child receives top-quality care
We are also state licensed as a Child Care facility and have met or exceeded all health and safety guidelines.
3-5 year Kinder Funded Program
Story Time
Show and Tell
Puzzles and Games
Computer Time
Arts and Crafts
Music
Pre-Reading Activities
And much more
You can rest assured that your child will be cared for with the most kindness, love and respect. We believe all children are precious gifts and we treat them as though they are our own.
Full-time, part-time, Half days, Before, after-school schedules are available.
To learn more, contact us today! 03 9481 -0576 or info@brightpebbles.example.au

```html
<!DOCTYPE html>
<html lang="en">
<head>
<meta charset="utf-8">
<title>Bright Pebbles Child Care and Kinder</title>
<link href="https://fonts.googleapis.com/css2?family=Varela+Round&family=Nunito:ital,wght@0,700;0,800;1,800&display=swap" rel="stylesheet">
<style>
:root{
  --sky:#b9e0f3;
  --sky-deep:#8fbad8;
  --sky-pale:#d2edf9;
  --pink:#d5a5cf;
  --pink-band:#c99ac6;
  --title-pink:#dc68a6;
  --navy:#24407a;
  --plum:#8a3f8d;
  --ink:#1f2a3a;
  --white:#ffffff;
}
*{margin:0;padding:0;box-sizing:border-box}
html,body{width:848px;height:1200px;overflow:hidden;background:var(--sky)}
.ad{position:relative;width:848px;height:1200px;overflow:hidden;background:var(--sky);font-family:"Varela Round",sans-serif;color:var(--white)}
.abs{position:absolute}
.header-sky{left:0;top:0;width:848px;height:180px;background:linear-gradient(180deg,#c7e8f7 0%,#b9e0f3 100%)}
.cloud{left:60px;top:92px;width:560px;height:70px;border-radius:60px;background:rgba(230,200,230,.55)}
.title{left:32px;top:52px;font-size:30px;color:var(--title-pink);letter-spacing:.3px}
.tagline{left:72px;top:100px;font-size:17px;color:var(--ink)}
.babies{left:640px;top:30px;width:88px;height:140px;border-radius:40px;background:linear-gradient(180deg,#d8b39a,#b98a6e)}
.butterfly{border-radius:50%;background:rgba(150,185,225,.55)}
.wave{left:0;top:165px;width:848px;height:72px}
.activities{left:0;top:182px;width:848px;text-align:center;font-size:16px;line-height:22px;color:var(--white)}
.activities span{margin:0 5px}
.middle{left:0;top:245px;width:848px;height:725px;background:linear-gradient(180deg,#9fc6e2 0%,#7fb0d4 55%,#98c3e0 100%)}
.headline{left:0;top:250px;width:848px;text-align:center;font-family:"Nunito",sans-serif;font-style:italic;font-weight:800;font-size:27px;letter-spacing:1px;color:var(--white);text-shadow:2px 2px 3px #1d3a5e}
.panel{background:var(--pink)}
.photo{background:var(--white);padding:10px;box-shadow:3px 4px 8px rgba(0,0,0,.35)}
.photo-fill{width:100%;height:100%}
.about-panel{left:306px;top:336px;width:542px;height:184px}
.about-photo{left:86px;top:332px;width:190px;height:190px;transform:rotate(-2deg)}
.h2{font-family:"Nunito",sans-serif;font-weight:800;font-size:27px;color:var(--navy)}
.about-title{left:315px;top:336px}
.body{font-size:16.5px;line-height:22px;color:var(--white)}
.about-copy{left:315px;top:374px;width:520px}
.programs-panel{left:0;top:551px;width:548px;height:162px}
.programs-title{left:34px;top:558px}
.programs-list{left:34px;top:602px;width:480px;display:grid;grid-template-columns:196px 1fr;row-gap:12px;font-size:18px;color:var(--white)}
.programs-photo{left:540px;top:530px;width:194px;height:182px;transform:rotate(3deg)}
.commit-panel{left:278px;top:740px;width:570px;height:158px}
.commit-title{left:290px;top:738px}
.commit-copy{left:290px;top:774px;width:548px}
.commit-photo{left:52px;top:742px;width:196px;height:196px;transform:rotate(-4deg)}
.footer-band{left:0;top:970px;width:848px;height:230px;background:var(--sky)}
.footer-strip{left:0;top:968px;width:848px;height:24px;background:var(--sky-pale)}
.contact{left:20px;top:994px;width:450px;text-align:center;font-family:"Nunito",sans-serif;font-weight:800;color:var(--plum);font-size:26px;line-height:38px}
.balloons{left:520px;top:880px;width:290px;height:300px;border-radius:48% 52% 30% 40%;background:radial-gradient(circle at 50% 35%,rgba(255,255,255,.95),rgba(255,255,255,.55) 60%,rgba(255,255,255,0) 75%)}
.badges{left:34px;top:1164px;font-size:18px;color:var(--title-pink)}
.badges span{margin-right:70px}
</style>
</head>
<body>
<div class="ad">
  <div class="abs header-sky"></div>
  <div class="abs cloud"></div>
  <div class="abs butterfly" style="left:120px;top:4px;width:46px;height:30px" role="img" aria-label="Small butterfly decoration"></div>
  <div class="abs butterfly" style="left:738px;top:40px;width:52px;height:40px" role="img" aria-label="Small butterfly decoration"></div>
  <div class="abs butterfly" style="left:785px;top:112px;width:36px;height:26px" role="img" aria-label="Small butterfly decoration"></div>
  <h1 class="abs title" style="font-weight:400">Bright Pebbles Child Care and Kinder</h1>
  <p class="abs tagline">We are not just a child Care Centre we are Family</p>
  <div class="abs babies" role="img" aria-label="Photo of three smiling babies sitting together"></div>

  <svg class="abs wave" viewBox="0 0 848 72" preserveAspectRatio="none" aria-hidden="true">
    <path d="M0 8 C200 0 420 22 848 6 L848 62 C520 76 300 52 0 66 Z" fill="var(--pink-band)"/>
    <path d="M0 66 C300 52 520 76 848 62 L848 72 L0 72 Z" fill="#e8d0e8"/>
  </svg>
  <p class="abs activities">
    <span>Story Time</span><span>Show and Tell</span><span>Puzzles and Games</span><span>Computer Time</span><span>Arts and Crafts</span><br>
    <span>Music</span><span>Pre-Reading Activities</span><span>And much more</span>
  </p>

  <div class="abs middle" role="img" aria-label="Soft blue background with a faint perspective grid pattern"></div>
  <p class="abs headline">A LIMITED NUMBER OF SPACES ARE AVAILABLE NOW!</p>

  <div class="abs panel about-panel"></div>
  <div class="abs photo about-photo"><div class="photo-fill" role="img" aria-label="Photo of a baby lying on a soft white blanket" style="background:linear-gradient(135deg,#f2e4dc,#d9bfae)"></div></div>
  <h2 class="abs h2 about-title">About Us</h2>
  <p class="abs body about-copy">Bright Pebbles Child Care Centre offers a safe, nurturing environment where your child will get the attention and care that he or she needs. Our ratio of children to adults is always within state guidelines - and often even higher - to make certain each child receives top-quality care</p>

  <div class="abs panel programs-panel"></div>
  <h2 class="abs h2 programs-title">Our Programs</h2>
  <div class="abs programs-list">
    <span>Full Time</span><span>Part Time (full or half day)</span>
    <span>After School</span><span>Before School</span>
    <span>Holiday</span>
  </div>
  <div class="abs photo programs-photo"><div class="photo-fill" role="img" aria-label="Photo of a child with colourful face paint" style="background:linear-gradient(135deg,#b7c9d8,#d9a98b)"></div></div>

  <div class="abs panel commit-panel"></div>
  <div class="abs photo commit-photo"><div class="photo-fill" role="img" aria-label="Photo of children playing with crafts in a classroom" style="background:linear-gradient(135deg,#d8c3b8,#8fa6c4)"></div></div>
  <h2 class="abs h2 commit-title">Our Committment</h2>
  <p class="abs body commit-copy">At Bright Pebbles we are focused on providing a quality service with the highest levels of customer satisfaction &amp; we will do everything we can to meet your expectations. With a variety of offerings to choose from, we're sure you'll be happy working with us.</p>

  <div class="abs footer-band"></div>
  <div class="abs footer-strip"></div>
  <div class="abs balloons" role="img" aria-label="Illustration of a child floating away holding a cloud of white butterflies"></div>
  <p class="abs contact">To learn more contact us today!<br>03 9481 -0576<br>or<br>info@brightpebbles.example.au</p>
  <p class="abs badges"><span>State Licensed</span>3-5 Kinder Funded Program</p>
</div>
</body>
</html>
```